Fleet Service Tri Fold Flyer

I am looking to come up with a flyer design to hand out showing our services. I will upload more info with working, but in the mean time want to just have a flyer to pass out. I have uploaded our logo and the images for it. I also uploaded what our trucks look like for ideas, as well as a business card.

Industry/Entity Type

Mobile Hydraulics and Fleet Service

Colors
0054AA
0677BA
7BADD7
CADEEF
E8F1F8
F0912C
F2A743
F7CA91
FBE8D2
FDF5EE

Requirements
Must have
• I uploaded a PDF with wording for the flyer

```html
<!DOCTYPE html>
<html lang="en">
<head>
<meta charset="utf-8">
<title>Ironline Fleet Service – Tri-Fold Flyer</title>
<link rel="stylesheet" href="https://fonts.googleapis.com/css2?family=Russo+One&family=Montserrat:wght@400;500;600;700&family=Oswald:wght@600&display=swap">
<style>
  :root{
    --navy:#0c4173;
    --navy-deep:#0a355f;
    --teal-deep:#0e4868;
    --blue:#0677BA;
    --blue-mid:#0054AA;
    --sky:#7BADD7;
    --sky-pale:#CADEEF;
    --ice:#E8F1F8;
    --orange:#F0912C;
    --gold:#F2A743;
    --red:#e0262b;
    --ink:#2b2f36;
    --grey:#9aa3ad;
    --page:#e4e7eb;
    --white:#ffffff;
  }
  *{box-sizing:border-box;margin:0;padding:0}
  html,body{width:1200px;height:1200px;overflow:hidden;background:var(--page)}
  body{position:relative;font-family:"Montserrat",sans-serif;color:var(--ink)}
  .sheet{position:absolute;left:190px;width:820px;height:578px;overflow:hidden;background:var(--white);box-shadow:0 6px 18px rgba(0,0,0,.22)}
  .sheet--outer{top:14px}
  .sheet--inner{top:608px}
  .abs{position:absolute}
  .panel-bg{position:absolute;top:0;height:578px}
  .fold{position:absolute;top:0;width:14px;height:578px;background:linear-gradient(90deg,rgba(0,0,0,.05),rgba(0,0,0,0));pointer-events:none}
  .shapes{position:absolute;left:0;top:0}
  .photo{position:absolute}

  .heading{font-family:"Russo One",sans-serif;color:var(--navy);letter-spacing:.2px}
  .body-text{font-size:9.4px;line-height:13.1px;text-align:justify;color:var(--ink)}
  .body-text p+p{margin-top:12px}

  /* outer sheet */
  .roadside{left:28px;top:24px;width:217px}
  .roadside .heading{font-size:15.5px;line-height:21px;margin-bottom:10px}
  .brand-name{font-family:"Russo One",sans-serif;text-align:center;letter-spacing:1px}
  .brand-name--cover{left:600px;top:58px;width:160px;font-size:17px;line-height:21px;color:var(--navy)}
  .brand-name--band{left:380px;top:398px;width:150px;font-size:15px;line-height:19px;color:var(--white)}
  .contact{left:300px;top:450px;width:228px;text-align:right;color:var(--white);font-size:10px}
  .contact__title{font-family:"Montserrat",sans-serif;font-weight:700;color:var(--gold);font-size:12px;letter-spacing:.5px;margin-right:16px;margin-bottom:4px}
  .contact__row{display:flex;justify-content:flex-end;align-items:center;gap:5px;line-height:13.5px;margin-top:3px}
  .contact__row svg{flex:none}
  .cover-copy{left:572px;top:394px;width:230px;color:var(--white)}
  .cover-copy__title{font-family:"Russo One",sans-serif;color:var(--gold);font-size:22px;line-height:27px;letter-spacing:.8px}
  .cover-copy__sub{font-weight:700;font-size:12.4px;line-height:19px;margin-top:12px}
  .cover-copy__url{font-weight:500;font-size:11.5px;margin-top:26px}
  .cover-copy__url span{color:var(--gold)}

  /* inner sheet */
  .services{left:28px;top:24px;width:230px}
  .services .heading{font-size:18.5px;letter-spacing:1px}
  .service{position:absolute;left:0;display:flex;align-items:center;width:240px}
  .service__icon{position:relative;width:54px;height:54px;flex:none}
  .service__num{position:absolute;left:-1px;top:-12px;width:20px;height:20px;border-radius:50%;background:var(--orange);color:var(--white);font-weight:700;font-size:12px;line-height:20px;text-align:center;border:1.5px solid var(--white)}
  .service__label{margin-left:9px;font-size:10.4px;line-height:13.5px;font-weight:500;color:#1d2430}
  .call{left:28px;top:528px;font-family:"Oswald",sans-serif;font-weight:600;font-size:14.5px;line-height:19px}
  .call__lead{color:var(--gold)}
  .call__phone{color:var(--white)}

  .hydraulic{left:301px;top:24px;width:218px}
  .hydraulic .heading{font-size:17px;line-height:21px;letter-spacing:.6px}
  .hours-badge{left:442px;top:24px}
  .hydraulic__lead{position:absolute;left:0;top:84px;width:230px;font-family:"Russo One",sans-serif;color:var(--red);font-size:14.5px;line-height:21px}
  .hydraulic .body-text{position:absolute;left:0;top:146px;width:218px}

  .steps{left:574px;top:24px;width:220px}
  .steps__title{font-weight:700;font-size:12.4px;color:var(--navy)}
  .step{position:absolute;left:0;display:flex;align-items:center;width:220px}
  .step__num{width:25px;height:25px;border-radius:50%;border:2px solid var(--blue-mid);color:var(--navy);font-weight:600;font-size:13px;line-height:21px;text-align:center;flex:none;background:var(--white)}
  .step__text{margin-left:10px;font-size:9.3px;line-height:12.8px;text-align:justify;width:183px}
  .steps .body-text{position:absolute;left:0;top:270px;width:218px}
</style>
</head>
<body>

<!-- Outer face -->
<section class="sheet sheet--outer" aria-label="Flyer outer face">
  <div class="panel-bg" style="left:0;width:273px;background:linear-gradient(180deg,#ffffff 0%,#ffffff 40%,#d9e7f4 100%)"></div>

  <div class="photo" role="img" aria-label="Photo of a yellow tracked excavator and a compact excavator on a sandy lot" style="left:0;top:0;width:400px;height:578px;background:linear-gradient(160deg,#6f8f5a 0%,#8aa36a 30%,#d4b443 50%,#c2ae86 70%,#e3d6bd 100%);clip-path:polygon(0 295px,210px 403px,392px 578px,0 578px)"></div>

  <div class="photo" role="img" aria-label="Photo of rental equipment lined up in a yard: skid steer, telehandler, compact tractor and dump trailer under trees" style="left:273px;top:0;width:547px;height:420px;background:linear-gradient(180deg,#dfe9f2 0%,#a9c1cf 18%,#5e7a4b 38%,#7b8a55 55%,#c9a444 66%,#d9c8a8 80%,#e7dbc3 100%)"></div>

  <svg class="shapes" width="820" height="578" viewBox="0 0 820 578" aria-hidden="true">
    <polygon points="183,402 547,318 820,400 820,412 547,330 190,412" fill="#9aa3ad"/>
    <polygon points="183,409 547,327 820,409 820,578 389,578" fill="var(--navy)"/>
    <polygon points="0,290 214,400 214,404 0,296" fill="#ffffff"/>
    <polygon points="183,409 389,578 381,578 176,411" fill="#9aa3ad"/>
  </svg>

  <div class="fold" style="left:273px"></div>
  <div class="fold" style="left:547px;background:linear-gradient(90deg,rgba(0,0,0,.1),rgba(0,0,0,0))"></div>

  <div class="abs roadside">
    <h2 class="heading">EMERGENCY ROADSIDE<br>ASSISTANCE:</h2>
    <div class="body-text">
      <p>Between our different locations we have several fully equipped &amp; stocked service trucks to meet your needs on the road. We offer onsite roadside repair &amp; diagnostics. Whether it’s during regular operating hours, after hours, weekends, or Holidays.</p>
      <p>We understand that your business depends on your truck being on the road and meeting your promised delivery schedule. Whether it’s at your shop, jobsite, or on the road, we are there to serve. We carry many of the common parts and items needed on the roadside.</p>
    </div>
  </div>

  <div class="abs brand-name brand-name--cover">IRONLINE FLEET SERVICE</div>
  <div class="abs brand-name brand-name--band">IRONLINE FLEET SERVICE</div>

  <div class="abs contact">
    <div class="contact__title">CONTACT US</div>
    <div class="contact__row"><span>4120 Cedar Mill Road,<br>Brookhaven, FL 33590</span>
      <svg width="11" height="11" viewBox="0 0 12 12"><circle cx="6" cy="6" r="5.4" fill="none" stroke="#F2A743" stroke-width="1"/><path d="M6 9.2C4.6 7.6 3.9 6.6 3.9 5.4a2.1 2.1 0 0 1 4.2 0c0 1.2-.7 2.2-2.1 3.8z" fill="none" stroke="#F2A743" stroke-width=".9"/></svg></div>
    <div class="contact__row"><span>1-888-555-0147</span>
      <svg width="11" height="11" viewBox="0 0 12 12"><circle cx="6" cy="6" r="5.4" fill="none" stroke="#F2A743" stroke-width="1"/><path d="M4 3.4l1 1.3-.6.8c.4.9 1.2 1.6 2 2l.8-.6 1.3 1-.6 1C5.6 8.8 3.3 6.5 3.1 4z" fill="#F2A743"/></svg></div>
    <div class="contact__row"><span>ops@ironlinerentals.com</span>
      <svg width="11" height="11" viewBox="0 0 12 12"><circle cx="6" cy="6" r="5.4" fill="none" stroke="#F2A743" stroke-width="1"/><rect x="3.3" y="4.2" width="5.4" height="3.8" fill="none" stroke="#F2A743" stroke-width=".9"/><path d="M3.3 4.2L6 6.3l2.7-2.1" fill="none" stroke="#F2A743" stroke-width=".9"/></svg></div>
    <div class="contact__row"><span>www.ironlinerentals.com</span>
      <svg width="11" height="11" viewBox="0 0 12 12"><circle cx="6" cy="6" r="5.4" fill="none" stroke="#F2A743" stroke-width="1"/><circle cx="6" cy="6" r="2.8" fill="none" stroke="#F2A743" stroke-width=".8"/><path d="M3.2 6h5.6M6 3.2v5.6" stroke="#F2A743" stroke-width=".7"/></svg></div>
  </div>

  <div class="abs cover-copy">
    <div class="cover-copy__title">RENTAL<br>COMPANY FOR</div>
    <div class="cover-copy__sub">LANDSCAPE, GARDENING<br>EQUIPMENT TO CONTRACTORS<br>AND TREE PROFESSIONALS.</div>
    <div class="cover-copy__url">www.<span>ironlinerentals</span>.com</div>
  </div>
</section>

<!-- Inner face -->
<section class="sheet sheet--inner" aria-label="Flyer inner face">
  <div class="panel-bg" style="left:0;width:274px;background:linear-gradient(180deg,#ffffff 0%,#e3edf7 45%,#f4f8fc 100%)"></div>
  <div class="panel-bg" style="left:274px;width:272px;background:linear-gradient(180deg,#ffffff 0%,#ffffff 60%,#e6eef6 100%)"></div>
  <div class="panel-bg" style="left:546px;width:274px;background:linear-gradient(180deg,#f3f7fb 0%,#ffffff 50%,#e4ecf4 100%)"></div>

  <svg class="shapes" width="820" height="578" viewBox="0 0 820 578" aria-hidden="true">
    <polygon points="0,463 250,538 250,545 0,470" fill="#9aa3ad"/>
    <polygon points="0,473 250,548 250,578 0,578" fill="var(--teal-deep)"/>
    <polygon points="505,463 820,352 820,362 505,472" fill="#9aa3ad"/>
    <polygon points="505,472 820,362 820,578 505,578" fill="var(--navy)"/>
  </svg>

  <div class="photo" role="img" aria-label="Photo of a white and blue mobile fleet service truck with a utility body" style="left:164px;top:424px;width:345px;height:154px;border-radius:10px 10px 0 0;background:linear-gradient(180deg,#eef2f6 0%,#dde4ec 40%,#1d4f86 62%,#163f6c 85%,#2c3a2a 100%);clip-path:polygon(0 60px,60px 40px,70px 0,345px 0,345px 154px,0 154px)"></div>

  <div class="photo" role="img" aria-label="Photo of a mechanic working under the open hood of a car in a workshop" style="left:505px;top:346px;width:315px;height:232px;background:linear-gradient(135deg,#c9d4dd 0%,#8797a6 35%,#2f3a46 60%,#151a21 100%);clip-path:polygon(0 126px,315px 16px,315px 232px,0 232px)"></div>

  <div class="fold" style="left:274px"></div>
  <div class="fold" style="left:546px"></div>

  <div class="abs services">
    <h2 class="heading">OUR SERVICES :</h2>

    <div class="service" style="top:42px">
      <div class="service__icon"><svg width="54" height="54" viewBox="0 0 54 54"><circle cx="27" cy="27" r="26" fill="var(--navy)"/><circle cx="27" cy="27" r="22" fill="none" stroke="#fff" stroke-width="1.2"/><rect x="20" y="15" width="14" height="24" rx="2" fill="none" stroke="#fff" stroke-width="1.4"/><circle cx="27" cy="25" r="4" fill="none" stroke="#fff" stroke-width="1.4"/><path d="M27 29v6" stroke="#fff" stroke-width="1.4"/></svg><span class="service__num">1</span></div>
      <div class="service__label">Mobile Hydraulic Repair</div>
    </div>
    <div class="service" style="top:113px">
      <div class="service__icon"><svg width="54" height="54" viewBox="0 0 54 54"><circle cx="27" cy="27" r="26" fill="var(--navy)"/><circle cx="27" cy="27" r="22" fill="none" stroke="#fff" stroke-width="1.2"/><path d="M14 26l7-6 6 4 6-4 7 6-9 9-4-3-4 3z" fill="none" stroke="#fff" stroke-width="1.4" stroke-linejoin="round"/></svg><span class="service__num">2</span></div>
      <div class="service__label">We come to you</div>
    </div>
    <div class="service" style="top:184px">
      <div class="service__icon"><svg width="54" height="54" viewBox="0 0 54 54"><circle cx="27" cy="27" r="26" fill="var(--navy)"/><circle cx="27" cy="27" r="22" fill="none" stroke="#fff" stroke-width="1.2"/><path d="M15 33v-5l3-5h10l3 5v5z" fill="none" stroke="#fff" stroke-width="1.4"/><path d="M24 22l2-4h9l3 5v5h-6" fill="none" stroke="#fff" stroke-width="1.4"/><circle cx="19" cy="34" r="2" fill="#fff"/><circle cx="27" cy="34" r="2" fill="#fff"/></svg><span class="service__num">3</span></div>
      <div class="service__label">Mobile Fleet Service and<br>repair at your yard or job site.</div>
    </div>
    <div class="service" style="top:255px">
      <div class="service__icon"><svg width="54" height="54" viewBox="0 0 54 54"><circle cx="27" cy="27" r="26" fill="var(--navy)"/><circle cx="27" cy="27" r="22" fill="none" stroke="#fff" stroke-width="1.2"/><path d="M14 35v-6l4-6h14l4 6v6z" fill="none" stroke="#fff" stroke-width="1.4"/><circle cx="34" cy="19" r="5" fill="var(--navy)" stroke="#fff" stroke-width="1.4"/><circle cx="19" cy="35" r="2" fill="#fff"/><circle cx="31" cy="35" r="2" fill="#fff"/></svg><span class="service__num">4</span></div>
      <div class="service__label">Complete Lube service, oil<br>changes, brake service and<br>more at your yard or job site.</div>
    </div>
    <div class="service" style="top:328px">
      <div class="service__icon"><svg width="54" height="54" viewBox="0 0 54 54"><circle cx="27" cy="27" r="26" fill="var(--navy)"/><circle cx="27" cy="27" r="22" fill="none" stroke="#fff" stroke-width="1.2"/><circle cx="29" cy="22" r="6" fill="none" stroke="#fff" stroke-width="2" stroke-dasharray="3 2"/><circle cx="29" cy="22" r="2.5" fill="none" stroke="#fff" stroke-width="1.2"/><path d="M14 34h8l6 3h10" fill="none" stroke="#fff" stroke-width="1.4"/></svg><span class="service__num">5</span></div>
      <div class="service__label">Roadside Assistance</div>
    </div>
    <div class="service" style="top:399px">
      <div class="service__icon"><svg width="54" height="54" viewBox="0 0 54 54"><circle cx="27" cy="27" r="26" fill="var(--navy)"/><circle cx="27" cy="27" r="22" fill="none" stroke="#fff" stroke-width="1.2"/><rect x="15" y="17" width="24" height="16" rx="1.5" fill="none" stroke="#fff" stroke-width="1.4"/><path d="M27 33v4M21 38h12" stroke="#fff" stroke-width="1.4"/><circle cx="27" cy="25" r="3.5" fill="none" stroke="#fff" stroke-width="1.6" stroke-dasharray="2 1.5"/></svg><span class="service__num">6</span></div>
      <div class="service__label">Advanced Computer</div>
    </div>
  </div>

  <div class="abs call">
    <div class="call__lead">Call us today!</div>
    <div class="call__phone">1-888-555-0147</div>
  </div>

  <div class="abs hydraulic">
    <h2 class="heading">MOBILE<br>HYDRAULIC<br>REPAIR :</h2>
    <div class="hydraulic__lead">Mobile Hose Repair Service,<br>24/7, 365 Days,</div>
    <div class="body-text">
      <p>Specializing in reducing customer’s equipment downtime and operating cost, by coming to you with a fully stocked truck and a mobile workshop.</p>
      <p>Ironline Mobile Hydraulic Repair provides the fastest hydraulic hose replacement and industrial hose repair service in the area. Our on site hydraulic repair is available 24/7, and is a simple solution that minimizes equipment downtime and eliminates the need for our customers to leave their job site or facility to locate a new hose. Our trucks are fully loaded with fittings and hoses to fix and make new hoses on demand exactly as the customer needs. We do it all on site and save you time from running around looking for a replacement hose.</p>
    </div>
  </div>

  <svg class="abs hours-badge" width="80" height="54" viewBox="0 0 80 54" aria-label="24 hours">
    <path d="M30 8A22 22 0 1 0 28 46" fill="none" stroke="var(--blue)" stroke-width="4"/>
    <path d="M20 14v14h10" fill="none" stroke="var(--navy)" stroke-width="3"/>
    <text x="31" y="36" font-family="Russo One, sans-serif" font-size="28" font-style="normal" fill="var(--navy)">24</text>
    <text x="30" y="48" font-family="Russo One, sans-serif" font-size="10" fill="var(--navy)">HOURS</text>
  </svg>

  <div class="abs steps">
    <div class="steps__title">The service technician will:</div>
    <div class="step" style="top:24px"><span class="step__num">1</span><span class="step__text">Quickley assess the situation and failure.</span></div>
    <div class="step" style="top:49px"><span class="step__num">2</span><span class="step__text">We will remove the failed hose to use it as a template to make a new one</span></div>
    <div class="step" style="top:89px"><span class="step__num">3</span><span class="step__text">The Truck is fully equipped to be able to custom fabricate a replacement hose to match exactly what you need.</span></div>
    <div class="step" style="top:140px"><span class="step__num">4</span><span class="step__text">We will then install the custom made hydraulic hose assembly on site without you ever having to move or transport the machine.</span></div>
    <div class="step" style="top:198px"><span class="step__num">5</span><span class="step__text">We will then work with the customer to ensure the equipment is up and running before leaving the jobsite.</span></div>
    <div class="body-text">
      <p>Our hydraulic hose repair service trucks are available day and night to fulfill your needs. To minimize your equipment downtime and operating costs, Ironline Fleet Service strives to be your go to call for on-location hydraulic hose replacement.</p>
    </div>
  </div>
</section>

</body>
</html>
```